Pelvin Advisory Business Card Design

Business card for business consulting company, using attached logo. We do financial and strategic consulting, and want a clean, professional image with a bit of fun. Our logo is a flat whale tail, which symbolizes the Orca whale, a highly collaborative, group based animal that is very successful in navigating the ocean, protecting the herd, and hunting. We like the logo that is blue and gray on white one one side, but would be open to a blue card with white lettering on the other side... or whatever you'd suggest
Updates
Hi all - I have had the logo modified to take the shadowing off the tail. I will post it on the brief... under a file name called updated logo. thank you Added Saturday, April 25, 2015
Target Market(s)
Small to medium sized businesses ($10M to $500M in revenue per year), financial and sales executives, general managers, attorneys and CPAs
Industry/Entity Type
Financial
Contact Information for Business Card
Want company name, contact info - name, title, telephone, email, website, linkedin, twitter and Facebook. No physical address yet.
Requirements
Must have
- contemporary design, bold, strong, confident but with a bit of fun. prominently feature the logo and the whale tail icon
Nice to have
- unique touches that would differentiate us from a regular card... for example, logo and writing all on front on white background, but on back - logo in white on a blue background
- open to idea of different shapes of card than standard... but not sure

```html
<!DOCTYPE html>
<html lang="en">
<head>
<meta charset="utf-8">
<title>Pelvin Advisory – Business Card</title>
<link rel="stylesheet" href="https://fonts.googleapis.com/css2?family=Arimo:wght@400&family=Open+Sans:wght@400;600&display=swap">
<style>
  :root {
    --page: #ffffff;
    --frame: #8a8a8a;
    --label: #111111;
    --card-blue: #0756a3;
    --card-shade: #074a8e;
    --ink-light: #ffffff;
    --mark-edge: rgba(255, 255, 255, 0.55);
  }
  * { margin: 0; padding: 0; box-sizing: border-box; }
  html, body {
    width: 1200px; height: 467px; overflow: hidden;
    background: var(--page);
  }
  .sheet {
    position: relative; width: 1200px; height: 467px;
    border: 1px solid var(--frame);
    font-family: "Arimo", Arial, sans-serif;
  }
  .side-label {
    position: absolute; top: 14px; width: 568px;
    text-align: center; font-size: 29px; color: var(--label);
  }
  .side-label--front { left: 20px; }
  .side-label--back { left: 611px; }

  .card {
    position: absolute; top: 59px; width: 568px; height: 368px;
    background: var(--card-blue); overflow: hidden; color: var(--ink-light);
  }
  .card--front { left: 20px; }
  .card--back { left: 611px; }

  /* Front: wordmark */
  .brand-mark {
    position: absolute; left: 103px; top: 153px;
    width: 62px; height: 62px; border-radius: 8px;
    border: 1px solid var(--mark-edge);
  }
  .brand-name {
    position: absolute; left: 172px; top: 143px;
    font-family: "Open Sans", Arial, sans-serif; font-weight: 600;
    font-size: 44px; letter-spacing: -0.5px; line-height: 1;
    color: var(--ink-light); white-space: nowrap;
  }
  .brand-tagline {
    position: absolute; left: 355px; top: 200px;
    font-family: "Open Sans", Arial, sans-serif;
    font-size: 12.5px; color: var(--ink-light); white-space: nowrap;
  }

  /* Back */
  .back-shade { position: absolute; left: 0; top: 0; }
  .person { position: absolute; right: 28px; top: 22px; text-align: right; }
  .person__name { font-size: 26px; letter-spacing: 0.3px; line-height: 1.1; }
  .person__title { font-size: 18px; margin-top: 6px; }

  .social { position: absolute; right: 30px; top: 107px; list-style: none; }
  .social__item {
    display: flex; align-items: center; justify-content: flex-end;
    height: 40px; margin-bottom: 14px; font-size: 18px;
  }
  .social__item:nth-child(2) { margin-bottom: 16px; }
  .social__dot {
    width: 41px; height: 41px; border-radius: 50%;
    background: var(--ink-light); margin-left: 10px;
  }

  .contact {
    position: absolute; right: 28px; top: 273px;
    list-style: none; text-align: right; font-size: 18px; line-height: 26px;
  }
</style>
</head>
<body>
<div class="sheet">
  <div class="side-label side-label--front">Front</div>
  <div class="side-label side-label--back">Back</div>

  <section class="card card--front" aria-label="Card front">
    <div class="brand-mark"></div>
    <div class="brand-name">pelvinadvisory</div>
    <div class="brand-tagline">business consulting</div>
  </section>

  <section class="card card--back" aria-label="Card back">
    <svg class="back-shade" width="568" height="368" viewBox="0 0 568 368" aria-hidden="true">
      <polygon points="65,125 285,125 172,368 0,368 0,205" fill="var(--card-shade)"/>
    </svg>

    <div class="person">
      <div class="person__name">MARCUS HALE</div>
      <div class="person__title">CEO</div>
    </div>

    <ul class="social">
      <li class="social__item">pelvinadv<span class="social__dot"></span></li>
      <li class="social__item">pelvinadv<span class="social__dot"></span></li>
      <li class="social__item">pelvinadv<span class="social__dot"></span></li>
    </ul>

    <ul class="contact">
      <li>+91 02200555014</li>
      <li>marcus@pelvinadvisory.in</li>
      <li>www.pelvinadvisory.com</li>
    </ul>
  </section>
</div>
</body>
</html>
```